Redesign Login page

I want to redesign my login page to bring my 2 products closer together. I am only looking to redesign one login page, not 2.

For the logo, please make it solid and it can be black or white if helpful. I can also fine tune the logo if you get it close.

Coding

Coded - Design and coding required

Number of Pages Required

1 page

```html
<!DOCTYPE html>
<html lang="en">
<head>
<meta charset="utf-8">
<title>Tealine – Login</title>
<link href="https://fonts.googleapis.com/css2?family=Ubuntu:wght@400;500&display=swap" rel="stylesheet">
<style>
  :root {
    --brand: #6f5a00;
    --brand-text: #6b5604;
    --ink: #3f3a28;
    --muted: #5e5a48;
    --cream: #fbf9e0;
    --field: #e6e4cb;
    --white: #ffffff;
    --shade: #3c3c3a;
  }
  * { box-sizing: border-box; margin: 0; padding: 0; }
  html, body { width: 1200px; height: 675px; overflow: hidden; }
  body { font-family: "Ubuntu", sans-serif; position: relative; background: var(--shade); }

  .hero-photo {
    position: absolute; left: 0; top: 0; width: 1200px; height: 590px;
    background:
      linear-gradient(180deg, rgba(70,70,68,0.95) 0%, rgba(70,70,68,0.9) 10%, rgba(60,78,76,0.85) 22%, rgba(74,82,70,0.8) 45%, rgba(40,60,40,0.9) 75%, rgba(20,32,24,0.95) 100%),
      radial-gradient(ellipse at 60% 70%, #4f6a2c 0%, #253a22 60%, #0f1a14 100%);
  }
  .footer-band { position: absolute; left: 0; top: 590px; width: 1200px; height: 85px; background: var(--shade); }

  .login-tab {
    position: absolute; left: 1046px; top: 29px; width: 87px; height: 34px;
    background: var(--white); color: var(--brand-text);
    font-size: 11.5px; font-weight: 500; text-align: center; line-height: 33px;
    border-radius: 2px 2px 0 0;
  }

  .login-panel {
    position: absolute; left: 805px; top: 62px; width: 328px; height: 413px;
    background: var(--white); border-radius: 4px 0 4px 4px; overflow: hidden;
  }
  .panel-head { height: 95px; text-align: center; padding-top: 22px; }
  .welcome { font-size: 9.5px; color: var(--brand-text); }
  .brand-name { margin-top: 8px; font-size: 24px; font-weight: 500; color: var(--brand); letter-spacing: 0.3px; }

  .panel-body { background: var(--cream); height: 313px; padding: 14px 28px 0 26px; position: relative; }
  .field-label { display: block; font-size: 9.5px; color: var(--ink); margin-left: 1px; }
  .field {
    display: block; width: 274px; height: 32px; margin-top: 3px; margin-bottom: 11px;
    background: var(--field); border: 0; border-radius: 2px;
    font-family: "Ubuntu", sans-serif; font-size: 7.5px; color: #9a9785; padding-left: 13px; line-height: 32px;
  }
  .btn-primary {
    display: block; width: 274px; height: 32px; margin-top: 5px; border-radius: 16px;
    background: var(--brand); color: var(--white); font-size: 12px; font-weight: 500;
    text-align: center; line-height: 31px;
  }
  .row { display: flex; justify-content: space-between; align-items: center; width: 274px; font-size: 9.5px; color: var(--ink); }
  .row.remember { margin-top: 14px; }
  .row.signup { margin-top: 15px; color: var(--muted); }
  .check { display: inline-block; width: 9px; height: 9px; background: var(--field); border-radius: 1px; margin-right: 6px; vertical-align: -1px; }
  .link { color: var(--brand-text); text-decoration: underline; }
  .or { text-align: center; width: 274px; font-size: 9px; color: var(--muted); margin-top: 15px; }
  .btn-alt {
    display: block; width: 274px; height: 32px; margin-top: 17px; margin-left: 1px; border-radius: 16px;
    background: var(--white); color: var(--brand-text); font-size: 11.5px; font-weight: 500;
    text-align: center; line-height: 31px;
  }
</style>
</head>
<body>
  <div class="hero-photo" role="img" aria-label="Blurred golf course scene with a golfer and green fairway behind a dark overlay"></div>
  <div class="footer-band"></div>

  <div class="login-tab">Login</div>

  <section class="login-panel">
    <header class="panel-head">
      <p class="welcome">Welcome to</p>
      <p class="brand-name">Tealine</p>
    </header>
    <div class="panel-body">
      <label class="field-label">User Name</label>
      <div class="field">Enter name</div>
      <label class="field-label">Password</label>
      <div class="field">Enter password</div>
      <div class="btn-primary">Sign in</div>
      <div class="row remember">
        <span><span class="check"></span>Remember Me</span>
        <span class="link">Forget Password</span>
      </div>
      <div class="row signup">
        <span>Don’t have an account ?</span>
        <span class="link">Sign Up</span>
      </div>
      <p class="or">OR</p>
      <div class="btn-alt">Sign in with Quorra</div>
    </div>
  </section>
</body>
</html>
```